Need a Revamped Website - WaveCrestline.com

I am looking for a website designed for www.wavecrestline.com
The present website has content relating to the Kabwe Airwave Gathering - an annual meeting for radio practitioners in Zambia. My intention is to change the focus: to make the website a resource hub for radio practitioners in Africa. The site is to have the following:
Featured articles (opinion pieces) contributed by industry insiders.
Links to various radio stations websites
An events calendar focusing on radio related events
News (radio industry updates) etc
The site should also be able to incorporate social media mechanisms such as 'Likes' through to plain square or articles to be shared on plain square etc.
The focus of the word Summit, for the purposes of the website, should shift. Instead of the meaning "meeting/ convention", it'll shift to connote "height, pinnacle (of radio excellence)".
The design should have a modern, contemporary feel.
Target Market(s)
The main target audience is radio deejays, radio station management, marketers/ advertisers, journalists.

```html
<!DOCTYPE html>
<html lang="en">
<head>
<meta charset="utf-8">
<title>Wave Crestline — Resource Hub for Radio Practitioners in Africa</title>
<link rel="stylesheet" href="https://fonts.googleapis.com/css2?family=Open+Sans:wght@300;400;600;700&family=Arimo:wght@400;700&display=swap">
<style>
:root{
  --orange:#f0a52c;
  --orange-deep:#e08d12;
  --brown:#3a2112;
  --brown-dark:#2a160b;
  --brown-text:#5a2d0c;
  --cream:#fcf1d9;
  --accent:#f29a12;
  --link:#e8921a;
  --ink:#222;
  --muted:#555;
  --panel-line:#d9d4cc;
  --bar:#efefef;
  --cal-dark:#5e3d27;
  --cal-light:#dcd6d0;
}
*{box-sizing:border-box;margin:0;padding:0}
html,body{width:975px;height:1200px;overflow:hidden}
body{position:relative;font-family:"Arimo",Arial,sans-serif;color:var(--ink);
  background:linear-gradient(180deg,#fdebc6 0,var(--cream) 180px,#fdf6e8 100%)}
a{color:inherit}

.top-nav{position:absolute;left:0;top:0;width:975px;height:48px;
  background:linear-gradient(#f4b441,var(--orange-deep));border-top:6px solid #d9d9d9;
  display:flex;justify-content:center;align-items:center;gap:0}
.top-nav a,.foot-nav a{text-decoration:none;font-weight:700;font-size:14px;letter-spacing:.3px}
.top-nav a{color:#4a2a10}
.top-nav a.current{color:#8a3f0a}
.star{font-size:12px;margin:0 25px;color:#3a2112}

.masthead{position:absolute;left:0;top:48px;width:975px;height:99px;background:var(--brown);border-bottom:1px solid #1c0e05}
.brand{position:absolute;left:34px;top:30px;font-family:"Open Sans",sans-serif;font-weight:700;font-size:33px;color:#fff;letter-spacing:-.5px}
.tagline{position:absolute;left:369px;top:39px;font-family:"Open Sans",sans-serif;font-size:12px;line-height:14px;color:#fff}
.search{position:absolute;left:758px;top:38px;width:176px;height:27px;border-radius:14px;background:#fff;box-shadow:inset 0 2px 3px #999}
.search svg{position:absolute;right:8px;top:6px}
.search::before{content:"";position:absolute;right:30px;top:4px;height:19px;border-left:1px solid #ccc}

.hero{position:absolute;left:27px;top:168px;width:918px;height:296px;background:#fff;border:1px solid #e4dccb;border-radius:3px}
.hero-stage{position:absolute;left:7px;top:7px;width:904px;height:280px;background:#efedec}
.hero-photo{position:absolute;left:26px;top:40px;width:500px;height:240px;
  background:radial-gradient(ellipse at 50% 60%,#6d5a4e 0,#8c7a6d 45%,#efedec 75%)}
.hero-copy{position:absolute;left:550px;top:98px;color:var(--brown-text);font-family:"Open Sans",sans-serif}
.hero-copy h1{font-size:20px;font-weight:700;letter-spacing:-.3px;margin-bottom:4px}
.hero-copy p{font-size:32px;font-weight:300;line-height:32px;letter-spacing:-.5px}
.hero-arrow{position:absolute;top:302px;width:36px;height:36px;border-radius:50%;background:#fff;border:1px solid #e4dccb;display:flex;align-items:center;justify-content:center}
.hero-arrow.prev{left:18px}.hero-arrow.next{left:920px}

.crumb{position:absolute;left:40px;top:478px;font-size:11px;display:flex;gap:8px;align-items:center}

.panel{position:absolute;background:#fff;border:1px solid var(--panel-line)}
.panel-head{height:36px;background:linear-gradient(#3b2314,var(--brown-dark));display:flex;align-items:center;justify-content:space-between;padding:0 10px 0 14px;color:#fff;font-size:14px;text-transform:uppercase}
.panel-head b{color:var(--accent)}
.panel-head .chip{background:#b0590c;color:#fff;font-size:11px;padding:2px 6px;text-transform:none;border:1px solid #d57a1f}
.copy{font-size:10.5px;line-height:14px;color:#333}
.more{color:var(--link);margin-left:6px}

.about{left:27px;top:500px;width:634px;height:158px}
.about .copy{padding:12px 13px 0;width:100%}
.about .narrow{width:430px}
.about .dishes{position:absolute;right:12px;bottom:6px;width:200px;height:60px;background:linear-gradient(90deg,rgba(255,255,255,0),#e4e4e4)}

.featured{left:27px;top:670px;width:634px;height:426px}
.article{padding:13px 13px 0;height:88px}
.article h3{font-size:11px;font-weight:700;margin-bottom:1px}
.meta{height:42px;background:var(--bar);display:flex;align-items:center;padding:0 13px;font-size:10.5px;gap:10px;color:#333}
.meta .sep{color:#888}
.meta a{text-decoration:underline}
.like{border:1px solid #b8c3d9;background:#eef1f7;color:#3b5998;padding:3px 6px;border-radius:2px;display:flex;gap:4px;align-items:center}
.sq{display:inline-block;width:11px;height:11px;background:#3b5998}
.sq.blue{background:#35b5e8}

.news{left:673px;top:500px;width:272px;height:405px}
.news-item{padding:12px 12px 0;border-bottom:1px solid #e2e2e2;height:123px}
.news-item:last-child{border:none}
.news-item h3{font-size:11px;font-weight:700;line-height:13px}
.news-item time{display:block;color:var(--link);font-size:9.5px;margin:3px 0 15px}

.events{left:673px;top:918px;width:272px;height:180px}
.events-title{position:absolute;left:12px;top:10px;font-family:"Open Sans",sans-serif;font-size:13px;line-height:13px;color:#3a2112}
.events-title b{display:block}
.events-icon{position:absolute;left:14px;top:45px;width:52px;height:56px;border:1px solid #c9b9a8;background:linear-gradient(#d66b2c 0 12px,#fbf6ef 12px)}
.events-mark{position:absolute;left:14px;top:106px;font-size:12px;font-weight:700;color:#c8c0b8;line-height:13px}
.cal-nav{position:absolute;left:14px;top:150px;display:flex;gap:3px}
.cal-nav span{width:16px;height:16px;border:1px solid #ccc;display:flex;align-items:center;justify-content:center;font-size:9px;color:#666}
.calendar{position:absolute;left:96px;top:10px;width:170px;border-collapse:separate;border-spacing:2px;background:#f4f0ec;font-size:10.5px;text-align:center}
.calendar caption{background:linear-gradient(#eee,#d7cfc6);font-weight:700;font-size:13px;padding:3px 0;color:#2a160b}
.calendar th{font-size:9px;background:#e9e5e1;height:13px}
.calendar td{background:var(--cal-light);height:18px;width:22px;font-weight:700;color:#222}
.calendar td.out{color:#999;background:#e4e0dc;font-weight:400}
.calendar td.hot{background:var(--cal-dark);color:#2a160b}
.calendar td.fade{background:#ebe8e5;color:#aaa;font-weight:400}

.footer{position:absolute;left:0;top:1112px;width:975px;height:88px;border-top:4px solid var(--orange-deep);background:var(--brown)}
.foot-nav{height:44px;display:flex;justify-content:center;align-items:center}
.foot-nav a{color:#fff}
.foot-nav .star{color:#fff}
.legal{height:40px;background:var(--brown-dark);color:#eee;font-size:11px;display:flex;justify-content:center;align-items:center;letter-spacing:.3px}
</style>
</head>
<body>

<nav class="top-nav">
  <a class="current" href="#">HOME</a><span class="star">★</span>
  <a href="#">ABOUT</a><span class="star">★</span>
  <a href="#">ARTICLES</a><span class="star">★</span>
  <a href="#">GALLERY</a><span class="star">★</span>
  <a href="#">PARTNERS</a><span class="star">★</span>
  <a href="#">EVENTS</a><span class="star">★</span>
  <a href="#">CONTACT</a>
</nav>

<header class="masthead">
  <div class="brand">WAVE CRESTLINE</div>
  <div class="tagline">BETTER PROGRAMMING. FREE SPEECH.<br>INTELLIGENT COMMUNICATION. GREAT ENTERTAINMENT</div>
  <div class="search">
    <svg width="14" height="14" viewBox="0 0 14 14"><circle cx="5.5" cy="5.5" r="4" fill="none" stroke="#333" stroke-width="2"/><line x1="8.5" y1="8.5" x2="13" y2="13" stroke="#333" stroke-width="2.4"/></svg>
  </div>
</header>

<section class="hero">
  <div class="hero-stage">
    <div class="hero-photo" role="img" aria-label="Group photo of seven smiling radio practitioners wearing lanyards"></div>
    <div class="hero-copy">
      <h1>WELCOME TO WAVE CRESTLINE</h1>
      <p>A RESOURCE HUB FOR<br>RADIO PRACTITIONERS<br>IN AFRICA</p>
    </div>
  </div>
</section>
<div class="hero-arrow prev"><svg width="10" height="12"><path d="M8 1 2 6l6 5z" fill="#2a160b"/></svg></div>
<div class="hero-arrow next"><svg width="10" height="12"><path d="M2 1l6 5-6 5z" fill="#2a160b"/></svg></div>

<div class="crumb">
  <svg width="10" height="10" viewBox="0 0 10 10"><path d="M5 1 1 5h1.5v4h5V5H9z" fill="#8a4a1a"/></svg>
  <span>Wave Crestline</span>
</div>

<section class="panel about">
  <div class="panel-head"><span>About <b>Wave Crestline</b></span></div>
  <p class="copy">Lorem ipsum dolor sit amet consectetur adipiscing elit. Sed accumsan tempus lobortis. Pellentesque habitant morbi tristique senectus et netus et malesuada fames ac turpis egestas.</p>
  <p class="copy narrow" style="padding:2px 13px 0">Fusce diam libero congue vel volutpat ut faucibus non arcu. Donec mollis sem nec mollis vehicula turpis turpis convallis velit nec volutpat tellus ante sit amet erat. Nunc ipsum lectus commodo in rutrum in suscipit ut lorem. Quisque vitae ipsum pharetra purus eleifend consectetur et id lorem. Praesent mollis magna id risus tristique sed facilisis quam egestas.<a class="more" href="#">read more...</a></p>
  <div class="dishes" role="img" aria-label="Row of satellite dishes fading into the background"></div>
</section>

<section class="panel featured">
  <div class="panel-head"><span>Featured <b>Articles</b></span><span class="chip">Read all</span></div>

  <article>
    <div class="article">
      <h3>Lorem ipsum dolor sit amet consectetur adipiscing elit.</h3>
      <p class="copy">Sed accumsan tempus lobortis. Pellentesque habitant morbi tristique senectus et netus et malesuada fames ac turpis egestas. Fusce diam libero congue volutpat. Praesent mollis magna id risus tristique sed facilisis quam egestas. Nulla congue, elit eget mattis fermentum, sem enim auctor lacus, quis viverra augue mauris sit amet enim.<a class="more" href="#">read more...</a></p>
    </div>
    <div class="meta">Posted by: <a href="#">Daniel Mwale</a><span class="sep">|</span>March 03, 2011<span class="sep">|</span><span class="like"><span class="sq"></span>Like</span><span class="sq"></span>3 people like this.<span class="sep">|</span>Share this on <span class="sq blue"></span></div>
  </article>

  <article>
    <div class="article">
      <h3>Lorem ipsum dolor sit amet consectetur adipiscing elit.</h3>
      <p class="copy">Sed accumsan tempus lobortis. Pellentesque habitant morbi tristique senectus et netus et malesuada fames ac turpis egestas. Fusce diam libero congue volutpat. Praesent mollis magna id risus tristique sed facilisis quam egestas. Nulla congue, elit eget mattis fermentum, sem enim auctor lacus, quis viverra augue mauris sit amet enim.<a class="more" href="#">read more...</a></p>
    </div>
    <div class="meta">Posted by: <a href="#">Daniel Mwale</a><span class="sep">|</span>March 03, 2011<span class="sep">|</span><span class="like"><span class="sq"></span>Like</span><span class="sq"></span>3 people like this.<span class="sep">|</span>Share this on <span class="sq blue"></span></div>
  </article>

  <article>
    <div class="article">
      <h3>Lorem ipsum dolor sit amet consectetur adipiscing elit.</h3>
      <p class="copy">Sed accumsan tempus lobortis. Pellentesque habitant morbi tristique senectus et netus et malesuada fames ac turpis egestas. Fusce diam libero congue volutpat. Praesent mollis magna id risus tristique sed facilisis quam egestas. Nulla congue, elit eget mattis fermentum, sem enim auctor lacus, quis viverra augue mauris sit amet enim.<a class="more" href="#">read more...</a></p>
    </div>
    <div class="meta">Posted by: <a href="#">Daniel Mwale</a><span class="sep">|</span>March 03, 2011<span class="sep">|</span><span class="like"><span class="sq"></span>Like</span><span class="sq"></span>3 people like this.<span class="sep">|</span>Share this on <span class="sq blue"></span></div>
  </article>
</section>

<aside class="panel news">
  <div class="panel-head"><span>Radio <b>News</b></span><span class="chip">RSS</span></div>
  <div class="news-item">
    <h3>Lorem ipsum dolor sit amet consectetur adipiscing elit.</h3>
    <time>March 24, 2011</time>
    <p class="copy">Pellentesque habitant morbi tristique senectus et netus et malesuada fames ac turpis egestas. Fusce diam libero congue vel volutpat ut faucibus non arcu.<a class="more" href="#">read more...</a></p>
  </div>
  <div class="news-item">
    <h3>Donec mollis sem nec mollis vehicula turpis turpis convallis velit nec.</h3>
    <time>March 24, 2011</time>
    <p class="copy">Nunc ipsum lectus commodo in rutrum in suscipit ut lorem. Quisque vitae ipsum pharetra purus eleifend consectetur et id lorem. Praesent mollis magna id risus tristique sed facilisis quam.<a class="more" href="#">read more...</a></p>
  </div>
  <div class="news-item">
    <h3>Nulla congue elit eget mattis fermentum, sem enim auctor lacus quis viverra.</h3>
    <time>March 24, 2011</time>
    <p class="copy">Proin laoreet rhoncus orci, nec sagittis odio ornare eget. Aenean ligula arcu, dapibus non fermentum ut iaculis sit amet massa.<a class="more" href="#">read more...</a></p>
  </div>
</aside>

<aside class="panel events">
  <div class="events-title">LATEST<b>EVENTS</b></div>
  <div class="events-icon" role="img" aria-label="Calendar page icon"></div>
  <div class="events-mark">WAVE<br>CREST</div>
  <div class="cal-nav"><span>◀</span><span>▶</span></div>
  <table class="calendar">
    <caption>April 2011</caption>
    <tr><th>S</th><th>M</th><th>T</th><th>W</th><th>T</th><th>F</th><th>S</th></tr>
    <tr><td class="out">27</td><td class="out">28</td><td class="out">29</td><td class="out">30</td><td class="out">31</td><td>1</td><td>2</td></tr>
    <tr><td>3</td><td>4</td><td>5</td><td>6</td><td>7</td><td>8</td><td>9</td></tr>
    <tr><td>10</td><td class="hot">11</td><td class="hot">12</td><td class="hot">13</td><td class="hot">14</td><td class="hot">15</td><td class="hot">16</td></tr>
    <tr><td class="hot">17</td><td>18</td><td>19</td><td>20</td><td>21</td><td>22</td><td>23</td></tr>
    <tr><td>24</td><td>25</td><td>26</td><td>27</td><td>28</td><td>29</td><td>30</td></tr>
    <tr><td class="fade">1</td><td class="fade">2</td><td class="fade">3</td><td class="fade">4</td><td class="fade">5</td><td class="fade">6</td><td class="fade">7</td></tr>
  </table>
</aside>

<footer class="footer">
  <nav class="foot-nav">
    <a href="#">HOME</a><span class="star">★</span>
    <a href="#">ABOUT</a><span class="star">★</span>
    <a href="#">ARTICLES</a><span class="star">★</span>
    <a href="#">GALLERY</a><span class="star">★</span>
    <a href="#">PARTNERS</a><span class="star">★</span>
    <a href="#">EVENTS</a><span class="star">★</span>
    <a href="#">CONTACT</a>
  </nav>
  <div class="legal">© Wave Crestline 2011.&nbsp; All Rights Reserved.&nbsp; Terms of Use.&nbsp; Privacy Policy.</div>
</footer>

</body>
</html>
```